Vell & Thorn Website Creation For Online Spirits Sales via MirrowDistillery.com

Want a Website developed that I will use to partner with Mirrow Distillery to sell my signature rum online. Mirrow Distillery will add the final code to make the website an e-commerce site. Website should have links to Social media pages, recipies, About, news and events, products. I have he domain name already just need a designer to make the website look professional. Need website capable of being viewed on iPhone and Android devices. Please use the color scheme that is on the label. The brand motto is: Celebrate Life With Family old and new friends. The bottle sent in the images will be replaced with and actual high resolution image of the bottle when it is produce on 27 DEC 21. Can give the selected designer access to develop the website. I have the hostiveno.com domain name. Final code will be added by a designer from MirrowDistillery.com to make it a e-commerce store.
Updates

I added more information to refine the design I wanted. I should have had this information available to the designers when I started the project.

Target Market(s)

Target Market is 25-50 year old who drink rum

Industry/Entity Type

Spirits. Using Website to sell Rum online

Number of Pages Required

1 page

Font styles to use
Sans Serif

Colors
00AB8E
00BBA5
67D7C9
C6EFE9
E9F9F6

Requirements
Must have
• Must look elegant and of high class. Rum is being market as a premium unnamed rum.
Nice to have
• Video of people drinking, smiling and celebrating

```html
<!DOCTYPE html>
<html lang="en">
<head>
<meta charset="utf-8">
<title>Vell &amp; Thorn — Premium Rum</title>
<link rel="stylesheet" href="https://fonts.googleapis.com/css2?family=Cinzel:wght@600;700&family=Roboto:wght@400;500;700&display=swap">
<style>
:root{
  --green:#17967a;
  --green-dark:#12846b;
  --mint:#5fd3be;
  --cream:#efe8d2;
  --cream-dark:#e0d8c0;
  --ink:#1b1b1b;
  --muted:#6b6b6b;
  --footer:#1d1d1d;
  --star:#f5a623;
  --white:#ffffff;
}
*{box-sizing:border-box;margin:0;padding:0}
html,body{width:1200px;height:4172px;overflow:hidden}
body{font-family:'Roboto',sans-serif;color:var(--ink);background:var(--cream);position:relative}
.serif{font-family:'Cinzel',serif}
.abs{position:absolute}
.btn{display:inline-flex;align-items:center;gap:8px;background:var(--green);color:var(--white);font-weight:700;border-radius:30px;text-transform:uppercase;font-size:15px}
.btn .arrow{width:14px;height:14px;border-radius:50%;background:var(--white);display:inline-block;position:relative}
.btn .arrow::after{content:"";position:absolute;left:4px;top:4px;width:4px;height:4px;border-top:2px solid var(--green);border-right:2px solid var(--green);transform:rotate(45deg)}
.section-title{font-family:'Cinzel',serif;font-weight:700;font-size:40px;letter-spacing:2px;text-align:center;width:100%}

/* top bar & header */
.topbar{top:0;left:0;width:1200px;height:36px;background:#111;color:var(--white);font-size:12px;text-align:center;line-height:36px}
.header{top:36px;left:0;width:1200px;height:85px;background:var(--cream)}
.brand{left:110px;top:12px;display:flex;flex-direction:column;align-items:center;gap:4px}
.brand-mark{width:36px;height:36px;border-radius:50%;background:var(--ink)}
.brand-name{font-family:'Roboto',sans-serif;font-weight:500;font-size:17px;letter-spacing:.5px}
.nav{left:343px;top:34px;display:flex;gap:28px;font-size:15px;font-weight:500}
.subscribe{left:810px;top:26px;padding:9px 22px;font-size:15px;text-transform:none}
.icons{left:978px;top:32px;display:flex;gap:14px}

/* hero */
.hero{top:121px;left:0;width:1200px;height:595px;background:linear-gradient(100deg,#c9c9c7 0%,#a9a9a7 45%,#5a5a58 75%,#2e2b2c 100%)}
.hero-visual{top:0;left:640px;width:560px;height:595px;background:radial-gradient(circle at 55% 45%,#c48a3c 0 14%,#3a2a38 30%,rgba(40,35,45,0) 70%)}
.hero-edge{left:0;bottom:-2px;width:1200px;height:34px}
.hero h1{left:110px;top:148px;font-family:'Cinzel',serif;font-weight:700;font-size:42px;line-height:48px;letter-spacing:1.5px;width:560px}
.hero h1 span{color:var(--green)}
.hero p{left:110px;top:310px;width:500px;font-size:16px;line-height:28px;font-weight:500}
.hero .btn{left:110px;top:396px;padding:14px 38px}

/* about */
.about-visual{top:820px;left:110px;width:417px;height:417px;border-radius:50%;background:radial-gradient(circle,#8a7156 0%,#4a3a2c 60%,#2a2018 100%)}
.about-title{left:593px;top:862px;font-family:'Cinzel',serif;font-weight:700;font-size:40px;letter-spacing:2px}
.about-text{left:593px;top:922px;width:490px;font-size:14px;line-height:26px;color:var(--muted)}
.about-text p+p{margin-top:8px}
.about .btn{left:593px;top:1143px;padding:13px 34px}

/* recipes */
.recipes-title{top:1313px;left:0}
.card{background:var(--white);border-radius:6px;box-shadow:0 3px 10px rgba(0,0,0,.12);overflow:hidden;text-align:center}
.recipe{top:1400px;width:306px;height:362px}
.recipe .photo{height:208px;margin:2px}
.card h3{font-size:18px;font-weight:700;margin-top:22px}
.card p{font-size:14px;line-height:24px;color:var(--muted);padding:10px 22px 0}

/* testimonials */
.testimonials{top:1919px;left:0;width:1200px;height:446px;background:var(--green)}
.testimonials .section-title{position:absolute;top:50px;color:var(--cream)}
.t-card{top:127px;width:408px;height:230px;background:var(--white);border-radius:26px;box-shadow:0 8px 18px rgba(0,0,0,.2)}
.t-avatar{top:183px;width:112px;height:112px;border-radius:50%;background:linear-gradient(135deg,#6b8aa8,#2b3a4d);border:4px solid var(--white)}
.t-quote{left:100px;top:22px;font-family:'Cinzel',serif;font-size:64px;color:var(--green);line-height:1}
.t-text{left:100px;top:80px;width:280px;font-size:14px;line-height:24px;color:var(--muted)}
.t-name{left:100px;top:160px;font-weight:500;font-size:16px}
.t-stars{left:100px;top:182px;color:var(--star);font-size:16px;letter-spacing:1px}
.chev{top:2141px}

/* products */
.products-title{top:2446px;left:0}
.product-visual{top:2543px;left:110px;width:424px;height:478px;background:radial-gradient(ellipse at 50% 55%,#c98f3d 0 18%,#5fd3be 40%)}
.play{top:2748px;left:285px;width:72px;height:72px;border-radius:50%;background:var(--green)}
.thumb{top:3040px;width:128px;height:89px;background:linear-gradient(135deg,#5a2a2a,#1e1414)}
.p-kicker{left:575px;top:2546px;font-size:14px;color:#444}
.p-name{left:573px;top:2564px;font-size:31px;font-weight:500}
.p-stars{left:575px;top:2604px;font-size:11px;color:var(--muted)}
.p-stars b{color:var(--star);font-weight:400;font-size:13px}
.p-price{left:576px;top:2630px;font-size:22px;font-weight:700;color:var(--green)}
.p-qty-label{left:576px;top:2690px;font-size:16px;font-weight:500}
.p-select{left:576px;top:2719px;width:490px;height:58px;background:#f1f1f1;border:1px solid #ddd;border-radius:4px;font-size:13px;color:var(--muted);padding:20px 24px}
.p-list{left:576px;top:2812px;font-size:14px;color:var(--muted);list-style:none}
.p-list li{display:flex;align-items:center;gap:14px;height:28px}
.p-list li::before{content:"";width:12px;height:12px;border-radius:50%;background:var(--green)}
.p-quote{left:576px;top:2920px;width:488px;height:94px;background:var(--white);border-radius:47px;padding:14px 30px 0 97px;font-size:14px;line-height:24px;color:var(--muted)}
.p-quote .avatar{position:absolute;left:10px;top:14px;width:64px;height:64px;border-radius:50%;background:linear-gradient(135deg,#8b6a52,#3c2a22)}
.add-cart{left:617px;top:3072px;width:428px;height:57px;justify-content:center;font-size:20px;text-transform:uppercase}

/* blog */
.blog-band{top:3511px;left:0;width:1200px;height:303px;background:var(--cream-dark)}
.blog-title{top:3240px;left:0}
.post{top:3317px;width:310px;height:387px;padding:7px}
.post .photo{height:203px;border-radius:3px}
.post .date{font-size:13px;color:var(--green);margin-top:26px}
.post h3{margin-top:8px}
.post p{padding:6px 18px 0}
.post .more{display:block;margin-top:10px;font-size:14px;font-weight:700;color:var(--green)}

/* footer */
.footer{top:3814px;left:0;width:1200px;height:358px;background:var(--footer);color:var(--white)}
.f-h{font-size:18px;font-weight:700;top:66px}
.f-contact{left:110px;top:110px;font-size:14px;list-style:none}
.f-contact li{display:flex;gap:18px;margin-bottom:18px;line-height:22px}
.f-contact li i{width:12px;height:12px;margin-top:5px;background:var(--green);border-radius:2px;flex:none}
.f-links{top:110px;font-size:14px;list-style:none;line-height:26px}
.f-email{left:713px;top:108px;width:237px;height:44px;border-radius:22px;background:var(--white);color:#888;font-size:12px;padding:14px 24px}
.f-submit{left:963px;top:108px;width:124px;height:44px;justify-content:center;font-size:16px}
.f-check{left:713px;top:178px;font-size:13px;font-weight:500;display:flex;gap:10px;align-items:center}
.f-check i{width:11px;height:11px;border:2px solid var(--white)}
.f-social{left:710px;top:218px;display:flex;gap:10px}
.f-social span{width:32px;height:32px;border-radius:50%;border:1.5px solid var(--white)}
.f-copy{top:318px;left:0;width:1200px;text-align:center;font-size:13px}
</style>
</head>
<body>

<div class="abs topbar">Lorem ipsum dolor sit amet, consectetur adipiscing</div>

<header class="abs header">
  <div class="abs brand"><span class="brand-mark"></span><span class="brand-name">VELL &amp; THORN</span></div>
  <nav class="abs nav"><span>Home</span><span>Shop</span><span>Gifts</span><span>Bottle Shop</span><span>Blog</span><span>Contact Us</span></nav>
  <span class="abs btn subscribe">Subscribe Club</span>
  <div class="abs icons">
    <svg width="16" height="16" viewBox="0 0 16 16"><circle cx="6.5" cy="6.5" r="5" fill="none" stroke="#1b1b1b" stroke-width="2"/><line x1="10" y1="10" x2="15" y2="15" stroke="#1b1b1b" stroke-width="2"/></svg>
    <svg width="16" height="16" viewBox="0 0 16 16"><circle cx="8" cy="4.5" r="3.5" fill="#1b1b1b"/><path d="M2 16c0-5 12-5 12 0z" fill="#1b1b1b"/></svg>
    <svg width="16" height="16" viewBox="0 0 16 16"><path d="M8 15L1.5 8.5A3.8 3.8 0 018 3a3.8 3.8 0 016.5 5.5z" fill="#1b1b1b"/></svg>
    <svg width="16" height="16" viewBox="0 0 16 16"><path d="M5 5V4a3 3 0 016 0v1h3v11H2V5z" fill="#1b1b1b"/></svg>
  </div>
</header>

<section class="abs hero">
  <div class="abs hero-visual" role="img" aria-label="Rum bottle with a glass of red wine, grapes and a corkscrew on slate"></div>
  <h1 class="abs">CELEBRATE LIFE WITH FAMILY, <span>OLD AND NEW FRIENDS</span></h1>
  <p class="abs">Lorem ipsum dolor sit amet, consectetur adipiscing elit, sed do tempor incididunt ut labore et dolore magna aliqua.</p>
  <span class="abs btn">Shop Now <i class="arrow"></i></span>
  <svg class="abs hero-edge" viewBox="0 0 1200 34" preserveAspectRatio="none"><path d="M0 20 L40 14 L80 22 L130 12 L180 20 L240 10 L300 18 L360 12 L420 22 L480 14 L540 20 L600 10 L660 18 L720 12 L780 22 L840 14 L900 20 L960 10 L1020 18 L1080 12 L1140 22 L1200 14 L1200 34 L0 34Z" fill="#efe8d2"/></svg>
</section>

<section class="about">
  <div class="abs about-visual" role="img" aria-label="Circular photo of bottles resting in dry straw"></div>
  <h2 class="abs about-title">ABOUT US</h2>
  <div class="abs about-text">
    <p>Lorem ipsum dolor sit amet, consectetur adipiscing elit, sed do eiusmod tempor incididunt ut labore et dolore magna aliqua. Ut enim ad minim veniam, quis nostrud exercitation ullamco laboris nisi ut aliquip ex ea commodo consequat.</p>
    <p>Duis aute irure dolor in reprehenderit in voluptate velit esse cillum dolore eu fugiat nulla pariatur. Excepteur sint occaecat cupidatat non proident, sunt in culpa qui officia deserunt mollit anim id est laborum.</p>
  </div>
  <span class="abs btn">Read More <i class="arrow"></i></span>
</section>

<h2 class="abs section-title recipes-title">OUR RECIPES</h2>
<article class="abs card recipe" style="left:110px"><div class="photo" role="img" aria-label="Friends dining outdoors at sunset under string lights" style="background:linear-gradient(180deg,#f2d08a,#a0582a)"></div><h3>Lorem ipsum dolor sit amet,</h3><p>Sed ut perspiciatis unde omnis iste natus error sit voluptatem accusantium doloremque laudantium,</p></article>
<article class="abs card recipe" style="left:447px"><div class="photo" role="img" aria-label="Group of friends toasting glasses over a dinner table" style="background:linear-gradient(180deg,#5a6670,#2e3338)"></div><h3>Lorem ipsum dolor sit amet,</h3><p>Sed ut perspiciatis unde omnis iste natus error sit voluptatem accusantium doloremque laudantium,</p></article>
<article class="abs card recipe" style="left:782px"><div class="photo" role="img" aria-label="Two women laughing with glasses of wine in a garden" style="background:linear-gradient(180deg,#7d9a6a,#c9a89a)"></div><h3>Lorem ipsum dolor sit amet,</h3><p>Sed ut perspiciatis unde omnis iste natus error sit voluptatem accusantium doloremque laudantium,</p></article>

<section class="abs testimonials">
  <h2 class="section-title">CLIENTS TESTIMONIAL</h2>
  <div class="abs t-card" style="left:178px">
    <span class="abs t-quote">“</span>
    <p class="abs t-text">Sed ut perspiciatis unde omnis iste natus sit voluptatem accusantium doloremque laudantium, totam rem aperiam,</p>
    <span class="abs t-name">Milo Reyes</span><span class="abs t-stars">★★★★★</span>
  </div>
  <div class="abs t-avatar" style="left:126px;top:180px" role="img" aria-label="Customer portrait"></div>
  <div class="abs t-card" style="left:667px">
    <span class="abs t-quote">“</span>
    <p class="abs t-text">Sed ut perspiciatis unde omnis iste natus sit voluptatem accusantium doloremque laudantium, totam rem aperiam,</p>
    <span class="abs t-name">Milo Reyes</span><span class="abs t-stars">★★★★★</span>
  </div>
  <div class="abs t-avatar" style="left:615px;top:180px" role="img" aria-label="Customer portrait"></div>
  <svg class="abs" style="left:42px;top:204px" width="20" height="34" viewBox="0 0 20 34"><path d="M17 3L4 17l13 14" fill="none" stroke="#efe8d2" stroke-width="4"/></svg>
  <svg class="abs" style="left:1138px;top:204px" width="20" height="34" viewBox="0 0 20 34"><path d="M3 3l13 14L3 31" fill="none" stroke="#efe8d2" stroke-width="4"/></svg>
</section>

<h2 class="abs section-title products-title">OUR PRODUCTS</h2>
<div class="abs product-visual" role="img" aria-label="Rum bottle on a mint background, product video"></div>
<div class="abs play"><svg width="72" height="72" viewBox="0 0 72 72"><path d="M29 22l22 14-22 14z" fill="#fff"/></svg></div>
<div class="abs thumb" style="left:110px" role="img" aria-label="Video thumbnail of wine bottles"></div>
<div class="abs thumb" style="left:258px;background:linear-gradient(135deg,#c9c3bb,#6a1e22)" role="img" aria-label="Row of bottles on a shelf"></div>
<div class="abs thumb" style="left:406px" role="img" aria-label="Bottles stored in a rack"></div>
<span class="abs p-kicker">NEW ARRIVAL</span>
<h3 class="abs p-name">Lorem ipsum dolor sit amet,</h3>
<span class="abs p-stars"><b>★★★★★</b> (25 Customer Reviews)</span>
<span class="abs p-price">$149.94</span>
<span class="abs p-qty-label">Quantity</span>
<div class="abs p-select">Choose Qty
  <svg class="abs" style="right:24px;top:22px" width="10" height="14" viewBox="0 0 10 14"><path d="M5 0l5 6H0zM5 14L0 8h10z" fill="#333"/></svg>
</div>
<ul class="abs p-list"><li>Sed ut perspiciatis unde omnis iste natus</li><li>Accusantium doloremque laudantium,</li><li>Totam rem aperiam, eaque ipsa quae ab illo</li></ul>
<div class="abs p-quote"><span class="avatar" role="img" aria-label="Reviewer portrait"></span>“ Lorem ipsum dolor sit amet, consectetur adipiscing elit, sed do eiusmod tempor incididunt ut labore et dolore magna aliqua.  nostrud exercitation ”</div>
<span class="abs btn add-cart">Add to Cart</span>

<div class="abs blog-band"></div>
<h2 class="abs section-title blog-title">OUR BLOG</h2>
<article class="abs card post" style="left:110px"><div class="photo" role="img" aria-label="Two friends laughing by a campfire with glasses" style="background:linear-gradient(180deg,#6c7a5a,#c2642a)"></div><div class="date">▦ February 2, 2021</div><h3>Lorem ipsum dolor sit amet,</h3><p>Sed ut perspiciatis unde omnis iste natus sit voluptatem accusantium</p><span class="more">READ MORE ➜</span></article>
<article class="abs card post" style="left:445px"><div class="photo" role="img" aria-label="Friends toasting at an outdoor table" style="background:linear-gradient(180deg,#8aa070,#4a3a2a)"></div><div class="date">▦ February 2, 2021</div><h3>Lorem ipsum dolor sit amet,</h3><p>Sed ut perspiciatis unde omnis iste natus sit voluptatem accusantium</p><span class="more">READ MORE ➜</span></article>
<article class="abs card post" style="left:779px"><div class="photo" role="img" aria-label="Two women enjoying wine on a hillside at dusk" style="background:linear-gradient(180deg,#d8b58a,#6a6258)"></div><div class="date">▦ February 2, 2021</div><h3>Lorem ipsum dolor sit amet,</h3><p>Sed ut perspiciatis unde omnis iste natus sit voluptatem accusantium</p><span class="more">READ MORE ➜</span></article>

<footer class="abs footer">
  <h4 class="abs f-h" style="left:110px">Contact Us</h4>
  <ul class="abs f-contact">
    <li><i style="border-radius:50% 50% 50% 0"></i><span>Lorem ipsum dolor sit consectetur<br>adipiscing elit</span></li>
    <li><i></i><span>info@vellandthorn.com</span></li>
    <li><i style="border-radius:50%"></i><span>555-014-2290</span></li>
    <li><i></i><span>1 (555) 018 - 3346</span></li>
  </ul>
  <h4 class="abs f-h" style="left:432px">Links</h4>
  <ul class="abs f-links" style="left:432px"><li>Home</li><li>Shop</li><li>Products</li><li>About Us</li><li>Blog</li><li>Offers</li></ul>
  <ul class="abs f-links" style="left:536px"><li>Terms &amp; Condition</li><li>Privacy Policy</li><li>Support</li><li>Site Map</li><li>Contact Us</li></ul>
  <h4 class="abs f-h" style="left:710px">Subscribe for Updates</h4>
  <div class="abs f-email">Email Address</div>
  <span class="abs btn f-submit">SUBMIT</span>
  <div class="abs f-check"><i></i>Yes, Please Contact me.</div>
  <div class="abs f-social" aria-label="Social media links"><span></span><span></span><span></span></div>
  <div class="abs f-copy">© 2021 Vell &amp; Thorn | All Rights Reserved</div>
</footer>

</body>
</html>
```